Inflatable Event Hirer requires Tri-Fold mini brochure

Brochure design required for UK based entertainment company offering a wide range of entertainment equipment for a broad range of customers including private customers, corporate customers and charities. Brochure must showcase a overview of our products including most popular products and unique items such as Bouncy Castles, Obstacle Courses, Slides, Rodeo Bulls and Dunk Tanks that are available for hire for a wide range of events including Birthdays, weddings, festivals, product launches and more. Brochure design idea's to compliment existing website design www.hopvalleyleisure.co.uk Brochure needs to be highly visual with wording kept minimal with easy read at forefront of design.

Target Market(s)

Young Families, young adults, schools.

Industry/Entity Type

Entertainment

Requirements
Must have
• An overview of our products we offer;
• Bouncy Castle
• Inflatable Slides
• Obstacle Courses
• Go Karts
• Climbing Walls
• Candy Carts *NEW*
• Mobile Bars *NEW*
• Trampolines
• Rodeo Bulls
• Dunk Tanks
• and much more....
• Emphasis on website/online booking/telephone number (0871 4956 382)
• UK Nationwide delivery with most European countries covered.
• £5 million public liability insurance as standard!
• BLPG accredited company
• WKSC accredited staff
Nice to have
• Pictures of events/parties etc.

```html
<!DOCTYPE html>
<html lang="en">
<head>
<meta charset="utf-8">
<title>Hop Valley Leisure – Tri-Fold Brochure</title>
<link href="https://fonts.googleapis.com/css2?family=Arimo:wght@400;700&family=Bungee&display=swap" rel="stylesheet">
<style>
  :root{
    --red:#e0242b; --green:#1faa4a; --lime:#b7d332; --magenta:#c4168c;
    --cyan:#15a9d6; --purple:#6b2a8c; --yellow:#e7e41c; --orange:#f37021;
    --teal:#169c9b; --grass:#7fc242; --white:#fff; --page:#ececec;
    --body:"Arimo", Arial, sans-serif; --display:"Bungee", "Arial Black", sans-serif;
  }
  *{box-sizing:border-box;margin:0;padding:0}
  html,body{width:1200px;height:1000px;overflow:hidden;background:var(--page)}
  .canvas{position:relative;width:1200px;height:1000px;font-family:var(--body)}
  .sheet{position:absolute;overflow:hidden;
    background:repeating-linear-gradient(90deg,
      var(--red) 0 22px,var(--green) 22px 44px,var(--lime) 44px 60px,var(--magenta) 60px 80px,
      var(--cyan) 80px 94px,var(--purple) 94px 112px,var(--yellow) 112px 128px,var(--green) 128px 148px,
      var(--red) 148px 162px,var(--lime) 162px 178px,var(--magenta) 178px 198px)}
  .sheet--inside{left:62px;top:57px;width:641px;height:453px}
  .sheet--outside{left:445px;top:475px;width:640px;height:452px}
  .wave{position:absolute;left:0;top:0;width:100%;height:100%}
  .photo{position:absolute;border-radius:50%;border:4px solid var(--white)}
  .figure{position:absolute;border-radius:40% 40% 30% 30%}
  .pill{position:absolute;height:21px;background:var(--white);border-radius:11px;
    font:700 10.5px/21px var(--body);text-align:center;white-space:nowrap}
  .new-star{position:absolute;width:26px;height:26px}
  .heading{position:absolute;font:15px/1 var(--display);letter-spacing:.5px;
    background:var(--white);padding:2px 4px;border-radius:3px;white-space:nowrap;z-index:2}
  .panel{position:absolute;border:3px solid var(--white);border-radius:18px;color:var(--white);
    font:700 7.8px/1.18 var(--body);padding:8px 9px;overflow:hidden}
  .panel p+p{margin-top:8px}
  .facts{text-align:center;font-size:10.5px;line-height:1.3;display:flex;flex-direction:column;justify-content:center;gap:12px}
  .cta{position:absolute;left:680px;width:170px;text-align:center}
  .cta-label{font:15px/1 var(--display);color:var(--white);letter-spacing:1px}
  .cta-label span{padding:1px 3px}
  .brand{position:absolute;left:902px;top:692px;width:120px;height:120px;border-radius:50%;
    background:var(--white);border:4px solid var(--purple);display:flex;align-items:center;justify-content:center;
    text-align:center;font:700 17px/1.05 var(--body);color:var(--purple)}
</style>
</head>
<body>
<div class="canvas">

  <!-- Inside spread -->
  <section class="sheet sheet--inside">
    <svg class="wave" viewBox="0 0 641 453" preserveAspectRatio="none" aria-hidden="true">
      <path d="M0 0H641V140C560 150 480 262 380 252C300 244 200 150 0 182Z" fill="#fff"/>
    </svg>
    <div class="figure" role="img" aria-label="Red jumping child silhouette" style="left:78px;top:8px;width:40px;height:72px;background:var(--red)"></div>
    <div class="figure" role="img" aria-label="Yellow jumping child silhouette" style="left:242px;top:12px;width:40px;height:46px;background:var(--yellow)"></div>
    <div class="figure" role="img" aria-label="Cyan jumping child silhouette" style="left:332px;top:66px;width:38px;height:60px;background:var(--cyan)"></div>
    <div class="figure" role="img" aria-label="Magenta jumping child silhouette" style="left:412px;top:12px;width:66px;height:72px;background:var(--magenta)"></div>
    <div class="figure" role="img" aria-label="Green jumping child silhouette" style="left:536px;top:36px;width:74px;height:72px;background:var(--grass)"></div>

    <div class="photo" role="img" aria-label="Photo: children sliding down an inflatable slide" style="left:6px;top:82px;width:98px;height:98px;background:radial-gradient(circle,#e7b9a0,#c98a6e)"></div>
    <div class="photo" role="img" aria-label="Photo: child lying on a red bouncy castle" style="left:102px;top:50px;width:118px;height:118px;background:radial-gradient(circle,#e9a27a,#c23a2a)"></div>
    <div class="photo" role="img" aria-label="Photo: child inside an inflatable tunnel" style="left:216px;top:82px;width:126px;height:126px;background:radial-gradient(circle,#d9c3ad,#5f8a3d)"></div>
    <div class="photo" role="img" aria-label="Photo: toddler on an inflatable slide" style="left:326px;top:142px;width:104px;height:104px;background:radial-gradient(circle,#f0d5b8,#3ab0c8)"></div>
    <div class="photo" role="img" aria-label="Photo: child playing in a ball pool" style="left:428px;top:138px;width:112px;height:112px;background:radial-gradient(circle,#e8c6a8,#2f73c2)"></div>
    <div class="photo" role="img" aria-label="Photo: inflatable climbing obstacle" style="left:534px;top:120px;width:98px;height:98px;background:radial-gradient(circle,#e9c240,#c9472f)"></div>

    <div class="pill" style="left:20px;top:192px;width:88px;color:var(--red)">Bouncy Castle</div>
    <div class="pill" style="left:116px;top:192px;width:78px;color:var(--cyan)">Trampolines</div>
    <div class="pill" style="left:20px;top:222px;width:90px;color:var(--magenta)">Inflatable Slides</div>
    <div class="pill" style="left:118px;top:222px;width:76px;color:var(--red)">Dunk Tanks</div>
    <div class="pill" style="left:20px;top:253px;width:100px;color:var(--orange)">Obstacle Courses</div>
    <div class="pill" style="left:128px;top:253px;width:66px;color:var(--grass)">Go Karts</div>
    <div class="pill" style="left:20px;top:284px;width:90px;color:var(--cyan)">Climbing Walls</div>
    <div class="pill" style="left:116px;top:284px;width:78px;color:var(--magenta)">Rodeo Bulls</div>
    <div class="pill" style="left:20px;top:316px;width:82px;color:var(--red)">Candy Carts</div>
    <svg class="new-star" style="left:98px;top:313px" viewBox="0 0 22 22"><polygon points="11,0 13.5,6 20,4 16,10 22,13 15.5,14.5 16,21 11,16.5 6,21 6.5,14.5 0,13 6,10 2,4 8.5,6" fill="var(--yellow)"/><text x="11" y="13.3" font-size="5" font-family="Arimo, sans-serif" font-weight="700" fill="var(--purple)" text-anchor="middle">NEW</text></svg>
    <div class="pill" style="left:133px;top:316px;width:60px;color:var(--grass)">Slides</div>
    <div class="pill" style="left:20px;top:351px;width:88px;color:var(--orange)">Gyroscope</div>
    <div class="pill" style="left:116px;top:351px;width:78px;color:var(--red)">Photo Booth</div>
    <div class="pill" style="left:20px;top:382px;width:62px;color:var(--cyan)">Ball Pools</div>
    <div class="pill" style="left:116px;top:382px;width:78px;color:var(--magenta);padding-left:8px">Mobile Bars</div>
    <svg class="new-star" style="left:99px;top:379px" viewBox="0 0 22 22"><polygon points="11,0 13.5,6 20,4 16,10 22,13 15.5,14.5 16,21 11,16.5 6,21 6.5,14.5 0,13 6,10 2,4 8.5,6" fill="var(--yellow)"/><text x="11" y="13.3" font-size="5" font-family="Arimo, sans-serif" font-weight="700" fill="var(--purple)" text-anchor="middle">NEW</text></svg>
    <div class="pill" style="left:50px;top:410px;width:114px;color:var(--purple)">and much more…</div>

    <div class="heading" style="left:256px;top:220px;color:var(--magenta)">SAFETY</div>
    <div class="panel" style="left:234px;top:236px;width:172px;height:102px;background:var(--magenta)">Your safety is of paramount importance to use, and our record is second-to-none; we take every safety precaution required of us and more. We are members of the National Inflatable Operators' Guild, and all our inflatables are ISTC tested.</div>
    <div class="heading" style="left:256px;top:342px;color:var(--green)">PROFESSIONALISM</div>
    <div class="panel" style="left:234px;top:358px;width:172px;height:78px;background:var(--orange)">All our staff are highly trained individuals. We have staff members that are SIA certified, licensed for alcohol sales, CRB certified and more. Staff are uniformed and first aid-trained as standard.</div>
    <div class="heading" style="left:506px;top:242px;color:var(--purple)">REPUTATION</div>
    <div class="panel" style="left:449px;top:258px;width:172px;height:200px;background:var(--purple)">We have employed Clearwell Plc to review our health &amp; safety policies, risk assessments, method statements and employment law. We have taken this step to ensure that we are always up-to-date on health and safety law not only for you the customer but also for our employees. This means we can demonstrate staff training and have integrated policies and procedures that not only improve customer safety, but everyone's safety. To ensure our continuing reputation, our staff are continually trained and assessed.</div>
  </section>

  <!-- Outside spread -->
  <section class="sheet sheet--outside">
    <svg class="wave" viewBox="0 0 640 452" preserveAspectRatio="none" aria-hidden="true">
      <path d="M25 452V120C25 80 10 40 0 20V0H195C180 40 200 70 240 95C330 150 470 190 640 200V250C450 262 265 330 215 452Z" fill="#fff"/>
    </svg>
  </section>

  <div class="heading" style="left:533px;top:502px;color:var(--teal)">RELIABILITY</div>
  <div class="panel" style="left:468px;top:518px;width:167px;height:88px;background:var(--teal)">We are an independent company but work alongside many other hirers, so if we don't have the equipment you require, we can almost always source it from one of our recommended partners, never letting you down.</div>

  <div class="figure" role="img" aria-label="Group of cheering people silhouettes" style="left:473px;top:604px;width:48px;height:46px;background:var(--purple)"></div>
  <div class="heading" style="left:508px;top:630px;color:var(--grass);font-size:14px;line-height:1.05;text-align:right">CUSTOMER<br>SATISFACTION</div>
  <div class="panel" style="left:466px;top:660px;width:170px;height:256px;background:var(--grass);padding-top:12px">
    <p>We believe that our success can only be measured by the success of your event and the enjoyment expressed by your guests - there is no greater reward than a happy customer! Hop Valley has achieved a 99.9% score for our services, rated at very or extremely professional for the overall experience.</p>
    <p>In comparison to our competitors, we achieved a score of 99.9% for our products being of high quality, rated from comparable to much better.</p>
    <p>Hop Valley Customer Services have been rated from very to extremely efficient and helpful at 94.8%. 100% of our customers surveyed agreed they would recommend our services to family, friends or other businesses.</p>
  </div>

  <div class="panel facts" style="left:680px;top:518px;width:170px;height:170px;background:var(--orange)">
    <div>UK Nationwide delivery with most European countries covered</div>
    <div>£5 million public liability insurance as standard!</div>
    <div>BLPG accredited company</div>
    <div>WKSC accredited staff</div>
  </div>

  <div class="cta" style="top:705px">
    <div class="cta-label"><span style="background:var(--purple)">BOOK ONLINE</span></div>
    <div style="font:700 16px/1.3 var(--body);color:var(--purple);margin-top:3px">hopvalleyleisure.co.uk</div>
  </div>
  <div class="cta" style="top:755px">
    <div class="cta-label"><span style="background:var(--green)">CALL US</span></div>
    <div style="font:700 19px/1.3 var(--body);color:var(--green);margin-top:3px">0871 4956 382</div>
  </div>

  <div class="photo" role="img" aria-label="Photo: two smiling boys on an inflatable" style="left:874px;top:516px;width:210px;height:186px;border-width:5px;background:radial-gradient(circle,#f0c9a8,#d9b04a 60%,#3d8fd1)"></div>
  <div class="brand">Hop<br>Valley</div>

</div>
</body>
</html>
```